Business Card Design

Very plain simple card, Plain modern font. Background. Grey fading to black. Large Bright lime green text. Saying.

TWR-ZA.COM

Small other details in white text.

Irish Horse Sales . Livery . Stud . Shows

Mark Dabrowski
TWR
Birch Lodge
Carrowmede Lane
Thistlecombe
Lincolnshire
LN4 7JX

Email. Twrzap@mailvale.co.uk
Tel. 07482 936504

Industry/Entity Type

Business

Contact Information for Business Card

As below

```html
<!DOCTYPE html>
<html lang="en">
<head>
<meta charset="utf-8">
<title>TWR-ZA.COM Business Card</title>
<link rel="stylesheet" href="https://fonts.googleapis.com/css2?family=Open+Sans:wght@600;700&display=swap">
<style>
  :root {
    --card-top: #b3b2b1;
    --card-mid: #5a5a5a;
    --card-bottom: #000000;
    --brand-green: #5dbb46;
    --text-white: #ffffff;
  }
  * { margin: 0; padding: 0; box-sizing: border-box; }
  html, body {
    width: 1200px;
    height: 791px;
    overflow: hidden;
    background: var(--card-bottom);
  }
  .business-card {
    position: relative;
    width: 1200px;
    height: 791px;
    background: linear-gradient(to bottom, var(--card-top) 0%, var(--card-mid) 42%, #1a1a1a 75%, var(--card-bottom) 95%);
    font-family: "Open Sans", "Segoe UI", sans-serif;
    color: var(--text-white);
  }
  .brand-name {
    position: absolute;
    left: 70px;
    top: 99px;
    font-size: 88px;
    line-height: 1;
    font-weight: 700;
    letter-spacing: -0.01em;
    color: var(--brand-green);
  }
  .details {
    position: absolute;
    font-size: 29px;
    line-height: 33.5px;
    font-weight: 700;
  }
  .tagline { left: 75px; top: 378px; }
  .address { left: 75px; top: 447px; font-style: normal; }
  .contact-line { left: 691px; }
  .contact-email { top: 581px; }
  .contact-phone { top: 648px; }
</style>
</head>
<body>
  <main class="business-card">
    <h1 class="brand-name">TWR-ZA.COM</h1>
    <p class="details tagline">Irish Horse Sales. Stud. Show</p>
    <address class="details address">
      Mark Dabrowski<br>
      TWR<br>
      Birch Lodge<br>
      Carrowmede Lane<br>
      Thistlecombe<br>
      Lincolnshire<br>
      LN4 7JX
    </address>
    <p class="details contact-line contact-email">Email. Twrzap@mailvale.co.uk</p>
    <p class="details contact-line contact-phone">Tel. 07482 936504</p>
  </main>
</body>
</html>
```